Business cards for education company

We need a business card design for a relatively new company based in Queensland and operating across Australia. We resell diploma level education courses which include Business, Management, Finance, Community Services & Government courses. We offer over 20 different courses.
The target market is for anyone 16 years of age and older. There is no age limit.

We would like to see the design use the color blue and silver. The final design should communicate professionalism and a bright future.

We sell education but are also promoting the career they see themselves in 2-3 years in the future

Our company logo is attached.

Target Market(s)

We target all age groups above 16 years of age. The main target market would be people aged between 17-35.

We focus on those people who cannot make it into University or do not want to commit the time to a full degree.

Industry/Entity Type

Education

Requirements
Must have
• Professional
Company logo
website
Contact details:

Please use the following example:

Lionel Parfitt
Senior Education Consultant
0417 386 591
Lionel.parfitt@brightwaylearninghub.com.au
www.brightwaylearninghub.com.au

```html
<!DOCTYPE html>
<html lang="en">
<head>
<meta charset="utf-8">
<title>Brightway Learning Hub – Business Card</title>
<link rel="stylesheet" href="https://fonts.googleapis.com/css2?family=Open+Sans:wght@400;600&display=swap">
<style>
  :root {
    --page: #ffffff;
    --card-white: #ffffff;
    --brand-blue: #1f4f9c;
    --accent-blue: #2a6fc9;
    --text-grey: #5a6a80;
    --silver-light: #f2f2f2;
    --silver-mid: #c9c9c9;
    --silver-dark: #9e9e9e;
    --edge: #3a3a3a;
  }
  * { margin: 0; padding: 0; box-sizing: border-box; }
  html, body {
    width: 1200px;
    height: 1200px;
    overflow: hidden;
    background: var(--page);
    font-family: "Open Sans", Arial, sans-serif;
  }
  .canvas {
    position: relative;
    width: 1200px;
    height: 1200px;
  }
  .business-card {
    position: absolute;
    left: 314px;
    top: 281px;
    width: 510px;
    height: 282px;
    border: 1.5px solid var(--edge);
    border-radius: 0 45px 0 45px;
    overflow: hidden;
    background: var(--card-white);
  }
  .card-header {
    position: absolute;
    left: 0; top: 0;
    width: 100%;
    height: 111px;
    background: var(--card-white);
  }
  .brand-mark {
    position: absolute;
    left: 26px;
    top: 34px;
    display: flex;
    align-items: center;
    gap: 12px;
  }
  .brand-dot {
    width: 38px;
    height: 38px;
    border-radius: 50%;
    background: var(--accent-blue);
  }
  .brand-name {
    font-size: 19px;
    font-weight: 600;
    color: var(--brand-blue);
    letter-spacing: 0.3px;
  }
  .header-rule {
    position: absolute;
    left: 0; top: 111px;
    width: 100%;
    height: 3px;
    background: var(--brand-blue);
  }
  .card-body {
    position: absolute;
    left: 0; top: 114px;
    width: 100%;
    height: 168px;
    background: linear-gradient(100deg,
      var(--silver-mid) 0%,
      var(--silver-light) 38%,
      #e4e4e4 55%,
      var(--silver-dark) 100%);
  }
  .contact-block {
    position: absolute;
    left: 205px;
    top: 57px;
    padding-left: 15px;
    border-left: 3px solid var(--brand-blue);
    height: 89px;
  }
  .contact-name {
    font-size: 19px;
    font-weight: 400;
    color: var(--brand-blue);
    letter-spacing: 0.6px;
    line-height: 20px;
  }
  .contact-role {
    margin-top: 5px;
    font-size: 13px;
    color: var(--text-grey);
    letter-spacing: 0.3px;
    line-height: 16px;
  }
  .contact-details {
    margin-top: 10px;
    list-style: none;
    font-size: 10.5px;
    font-weight: 600;
    color: var(--brand-blue);
    letter-spacing: 0.4px;
    line-height: 12px;
  }
</style>
</head>
<body>
  <main class="canvas">
    <article class="business-card">
      <header class="card-header">
        <div class="brand-mark">
          <span class="brand-dot"></span>
          <span class="brand-name">Brightway Learning Hub</span>
        </div>
      </header>
      <div class="header-rule"></div>
      <section class="card-body">
        <div class="contact-block">
          <h1 class="contact-name">Lionel Parfitt</h1>
          <p class="contact-role">Senior Education Consultant</p>
          <ul class="contact-details">
            <li>0417 386 591</li>
            <li>Lionel.parfitt@brightwaylearninghub.com.au</li>
            <li>www.brightwaylearninghub.com.au</li>
          </ul>
        </div>
      </section>
    </article>
  </main>
</body>
</html>
```